Business card for Northland's Blue Wagon.

Good day i am looking for a business card design for my business.
The name of the business is Northland's Blue Wagon. It is a van rental business that provides a driver and helper to the customer. Customer have use to van for small moves, studio or 1 bedroom, Moving furniture like couch or kitchen cabinets.
We are available evenings, weekends and holidays.
the means to contact us is by phone at 628-947-2071; By emails at Oakridge@northlandsbluewagon.net; or by social media, Facebook and Instagram.
You can see attached pictures of the van and or logo.

```html
<!DOCTYPE html>
<html lang="en">
<head>
<meta charset="utf-8">
<title>Northland's Blue Wagon – Business Card</title>
<link href="https://fonts.googleapis.com/css2?family=Montserrat:wght@500;700&display=swap" rel="stylesheet">
<style>
  :root {
    --page: #ebeaea;
    --card-red: #c42a20;
    --card-red-deep: #a81e17;
    --ink: #000000;
    --paper: #ffffff;
    --accent: #d7261c;
    --photo-top: #d9d9d9;
    --photo-mid: #c3241b;
    --photo-low: #3a3a3a;
  }
  * { box-sizing: border-box; margin: 0; padding: 0; }
  html, body {
    width: 1200px; height: 1145px; overflow: hidden;
    background: var(--page);
    font-family: "Montserrat", Arial, sans-serif;
  }
  .sheet {
    position: relative; width: 1200px; height: 1145px;
  }
  .card {
    position: absolute; left: 150px; width: 900px; height: 515px;
    background: radial-gradient(ellipse at 50% 50%, var(--card-red) 60%, var(--card-red-deep) 130%);
    overflow: hidden;
    box-shadow: 0 6px 16px rgba(0,0,0,.25);
  }
  .card--front { top: 30px; }
  .card--back { top: 600px; }

  /* front side */
  .logo-panel {
    position: absolute; left: 600px; top: 148px; width: 300px; height: 222px;
    background: var(--paper);
    border-radius: 111px 0 0 111px;
    display: flex; align-items: center; justify-content: center; gap: 10px;
    padding-left: 60px; padding-right: 16px;
  }
  .logo-dot {
    flex: none; width: 22px; height: 22px; border-radius: 50%;
    background: var(--accent);
  }
  .logo-name {
    font-weight: 700; font-size: 20px; line-height: 1.2; color: var(--ink);
  }
  .info-band {
    position: absolute; left: 0; top: 122px; width: 655px; height: 272px;
    background: var(--ink);
    border-radius: 0 136px 136px 0;
    padding: 52px 0 0 57px;
    color: var(--paper);
  }
  .company-name {
    font-weight: 700; font-size: 38px; letter-spacing: .3px; line-height: 1;
    margin-bottom: 26px;
  }
  .contact-list { list-style: none; }
  .contact-item {
    display: flex; align-items: center; gap: 14px;
    font-weight: 500; font-size: 20px; line-height: 30px;
  }
  .contact-icon { width: 16px; height: 16px; flex: none; }

  /* back side */
  .feature-band {
    position: absolute; left: 40px; top: 120px; width: 860px; height: 275px;
    background: var(--paper);
    border-radius: 137px 0 0 137px;
    overflow: hidden;
  }
  .van-photo {
    position: absolute; left: 20px; top: 20px; width: 420px; height: 270px;
    border-radius: 120px 20px 0 120px;
    background: linear-gradient(180deg, var(--photo-top) 0%, var(--photo-mid) 30%, var(--photo-mid) 70%, var(--photo-low) 100%);
  }
  .taglines {
    position: absolute; right: 36px; top: 70px;
    text-align: right; font-weight: 700; font-size: 28px; line-height: 53px;
    color: var(--ink);
  }
  .tag-bar {
    position: absolute; right: 0; top: 80px; width: 20px; height: 125px;
    background: var(--ink);
  }
</style>
</head>
<body>
<main class="sheet">

  <section class="card card--front" aria-label="Business card front">
    <div class="logo-panel">
      <span class="logo-dot"></span>
      <span class="logo-name">Northland's<br>Blue Wagon</span>
    </div>
    <div class="info-band">
      <h1 class="company-name">Northland's Blue Wagon</h1>
      <ul class="contact-list">
        <li class="contact-item">
          <svg class="contact-icon" viewBox="0 0 16 16" aria-hidden="true"><path fill="#d7261c" d="M3.3 1.2l2.2 2.6c.3.4.3.9 0 1.2L4.4 6.2c.9 2 2.4 3.5 4.4 4.4l1.2-1.1c.3-.3.8-.3 1.2 0l2.6 2.2c.4.3.4.9.1 1.3l-1.2 1.3c-.6.6-1.6.8-2.4.4C6.6 13.3 2.7 9.4 1.3 5.7c-.3-.8-.1-1.8.5-2.4L3 1.1c.1 0 .2.1.3.1z"/></svg>
          +1 628-947-2071
        </li>
        <li class="contact-item">
          <svg class="contact-icon" viewBox="0 0 16 16" aria-hidden="true"><circle cx="8" cy="8" r="6.5" fill="none" stroke="#d7261c" stroke-width="1.6"/><circle cx="8" cy="8" r="2.6" fill="none" stroke="#d7261c" stroke-width="1.6"/></svg>
          Oakridge@northlandsbluewagon.net
        </li>
        <li class="contact-item">
          <svg class="contact-icon" viewBox="0 0 16 16" aria-hidden="true"><g fill="none" stroke="#d7261c" stroke-width="1.4"><circle cx="8" cy="8" r="6.5"/><ellipse cx="8" cy="8" rx="3" ry="6.5"/><path d="M1.5 8h13M2.5 4.8h11M2.5 11.2h11"/></g></svg>
          www.northlandsbluewagon.net
        </li>
      </ul>
    </div>
  </section>

  <section class="card card--back" aria-label="Business card back">
    <div class="feature-band">
      <div class="van-photo" role="img" aria-label="Photo of the company's lettered cargo van"></div>
      <p class="taglines">Your friend with the van<br>Van rental with driver<br>Evenings and weekeands</p>
      <span class="tag-bar"></span>
    </div>
  </section>

</main>
</body>
</html>
```